Eye catching Bottle label for pink gin targeting women 25+

We need a new label for a re-launch of our shimmering strawberry pink gin liqueur. We would like it to look premium and eye catching on the shelf. We have 2 labels we require, one for 200ml bottle (2x2 inches) and one for 500ml bottle 4x4 inches). Label must state the ml of the bottle abd that it is 18.75%Vol. Also say Shimmering Strawberry Gin Liqueur with the brand name at the top - Harlow Vale Distillers. We have a logo but it doesn't need to be used if it doesn't work with the design/colours. The gin is presented in a clear bottle and is pink and sparkly. See uploaded image for reference.

Target Market(s)

Women aged 25-45

Font styles to use
Decorative

Colors
f59296
fbd4d5
eea4c8

Requirements
Must have
• Bottle size - 500ml/200ml
• Must say 18.75% Vol
• Must have brand name - Harlow Vale Distillers
• Must have product name - Shimmering Pink Strawberry
• Must say - Gin Liqueur
Nice to have
• Some sort of floral or swirley background detail would be nice
Should not have
• Must not appeal to children

```html
<!DOCTYPE html>
<html lang="en">
<head>
<meta charset="utf-8">
<title>Harlow Vale Distillers – Shimmering Pink Strawberry Gin Liqueur Labels</title>
<link rel="stylesheet" href="https://fonts.googleapis.com/css2?family=Arimo:wght@700&family=Parisienne&display=swap">
<style>
  :root {
    --board: #a7a9ac;
    --label-white: #ffffff;
    --salmon: #f59296;
    --blush: #fbd4d5;
    --orchid: #eea4c8;
    --ink: #111111;
    --brick: #b5553f;
    --foliage: #4f6b3a;
  }
  html, body {
    margin: 0;
    padding: 0;
    width: 1200px;
    height: 1200px;
    overflow: hidden;
    background: var(--board);
  }
  .canvas {
    position: relative;
    width: 1200px;
    height: 1200px;
  }
  .label {
    position: absolute;
    display: block;
  }
  .label--small { left: 208px; top: 160px; width: 172px; height: 172px; }
  .label--large { left: 54px; top: 516px; width: 432px; height: 432px; }
  .script {
    font-family: "Parisienne", cursive;
    fill: var(--ink);
  }
  .brand-name { font-size: 25px; }
  .product-type { font-size: 48px; }
  .detail {
    font-family: "Arimo", Arial, sans-serif;
    font-weight: 700;
    fill: var(--label-white);
  }
  .product-name { font-size: 13px; }
  .strength { font-size: 14px; }
  .bottle-photo {
    position: absolute;
    left: 528px;
    top: 58px;
    width: 609px;
    height: 1079px;
    background: linear-gradient(180deg, var(--brick) 0%, #c9705a 35%, #d98a92 55%, var(--foliage) 80%, #6f8f96 100%);
  }
</style>
</head>
<body>
<main class="canvas">

  <svg class="label label--small" viewBox="0 0 360 360" xmlns="http://www.w3.org/2000/svg" aria-label="200ml label">
    <defs>
      <linearGradient id="corner-tone-small" x1="0" y1="0" x2="1" y2="1">
        <stop offset="0" stop-color="#f5a3ab"/>
        <stop offset="0.5" stop-color="#fbd4d5"/>
        <stop offset="1" stop-color="#f2a9c6"/>
      </linearGradient>
    </defs>
    <rect x="0" y="0" width="360" height="360" fill="var(--label-white)"/>
    <rect class="floral-corners" x="12" y="12" width="336" height="336" fill="url(#corner-tone-small)" role="img" aria-label="Pink and white floral tile pattern in the label corners"/>
    <polygon class="diamond-panel" points="180,12 348,180 180,348 12,180" fill="var(--salmon)" stroke="var(--label-white)" stroke-width="6"/>
    <text class="script brand-name" x="180" y="78" text-anchor="middle">Harlow Vale</text>
    <text class="script brand-name" x="180" y="104" text-anchor="middle">Distillers</text>
    <text class="detail product-name" x="180" y="145" text-anchor="middle">Shimmering  Pink Strawberry</text>
    <text class="script product-type" x="180" y="212" text-anchor="middle">Gin Liqueur</text>
    <text class="detail strength" x="180" y="290" text-anchor="middle">18.75% Vol</text>
    <text class="detail strength" x="180" y="310" text-anchor="middle">200ml</text>
  </svg>

  <svg class="label label--large" viewBox="0 0 360 360" xmlns="http://www.w3.org/2000/svg" aria-label="Large label">
    <defs>
      <linearGradient id="corner-tone-large" x1="0" y1="0" x2="1" y2="1">
        <stop offset="0" stop-color="#f5a3ab"/>
        <stop offset="0.5" stop-color="#fbd4d5"/>
        <stop offset="1" stop-color="#f2a9c6"/>
      </linearGradient>
    </defs>
    <rect x="0" y="0" width="360" height="360" fill="var(--label-white)"/>
    <rect class="floral-corners" x="12" y="12" width="336" height="336" fill="url(#corner-tone-large)" role="img" aria-label="Pink and white floral tile pattern in the label corners"/>
    <polygon class="diamond-panel" points="180,12 348,180 180,348 12,180" fill="var(--salmon)" stroke="var(--label-white)" stroke-width="6"/>
    <text class="script brand-name" x="180" y="78" text-anchor="middle">Harlow Vale</text>
    <text class="script brand-name" x="180" y="104" text-anchor="middle">Distillers</text>
    <text class="detail product-name" x="180" y="145" text-anchor="middle">Shimmering  Pink Strawberry</text>
    <text class="script product-type" x="180" y="212" text-anchor="middle">Gin Liqueur</text>
    <text class="detail strength" x="180" y="290" text-anchor="middle">18.75% Vol</text>
    <text class="detail strength" x="180" y="310" text-anchor="middle">200ml</text>
  </svg>

  <div class="bottle-photo" role="img" aria-label="Photograph of the labelled pink shimmering gin liqueur bottle standing in a planter against a brick wall"></div>

</main>
</body>
</html>
```